Quorenta - Automated robotic Inspection with AI need new business cards

We need a new design of our business cards. The company is focused on automated quality control at high speed with unmatched results. We have a logo but need a more forward leaning business card that shows that we are delivering cutting edge technology.

Contact Information for Business Card

Name
Position
Adress
Phone
Email
e.g.
Lotta Berglund
Chief Financial Officer (CFO)

Quorenta Sweden AB
Rönnvägen 14, SE-175 43 JÄRFÄLLA, Sweden
Mobile: +46701 23 45 67 | Office: +46 8 52 61 74
www.quorenta-example.com

Font styles to use
Sans Serif

```html
<!DOCTYPE html>
<html lang="en">
<head>
<meta charset="UTF-8">
<title>Quorenta – Business Card</title>
<link rel="stylesheet" href="https://fonts.googleapis.com/css2?family=Lato:wght@400;700&display=swap">
<style>
  :root {
    --canvas-bg: #d9dadc;
    --card-white: #f4f5f7;
    --brand-blue: #2f5a91;
    --brand-blue-dark: #2a4f80;
    --card-blue: #3e6391;
    --text-dark: #2a2c30;
    --rule: #2a2c30;
  }
  * { margin: 0; padding: 0; box-sizing: border-box; }
  html, body {
    width: 1200px; height: 1200px; overflow: hidden;
    background: var(--canvas-bg);
    font-family: "Lato", sans-serif;
  }
  .sheet {
    width: 1200px; height: 1200px;
    display: flex; flex-direction: column;
    align-items: center; justify-content: center; gap: 60px;
  }
  .card {
    width: 900px; height: 514px; position: relative;
    box-shadow: 0 14px 30px rgba(0,0,0,0.18);
  }
  .card--back {
    background: var(--card-blue);
    display: flex; align-items: center; justify-content: center;
  }
  .card--front { background: var(--card-white); }

  .wordmark {
    display: flex; align-items: center; gap: 16px;
    font-weight: 700; letter-spacing: 2px;
  }
  .wordmark__dot { border-radius: 50%; flex: none; }
  .wordmark--back { font-size: 64px; color: var(--brand-blue-dark); }
  .wordmark--back .wordmark__dot { width: 44px; height: 44px; background: var(--brand-blue-dark); }
  .wordmark--front {
    position: absolute; left: 80px; top: 230px;
    font-size: 40px; color: var(--brand-blue);
  }
  .wordmark--front .wordmark__dot { width: 30px; height: 30px; background: var(--brand-blue); }

  .divider {
    position: absolute; left: 470px; top: 120px;
    width: 2px; height: 290px; background: var(--rule);
  }
  .details {
    position: absolute; left: 498px; top: 118px;
    color: var(--text-dark); font-size: 21px; line-height: 29px;
  }
  .details__name { font-size: 30px; font-weight: 700; color: var(--brand-blue); line-height: 36px; }
  .details__role { margin-bottom: 12px; }
  .details__company { color: var(--brand-blue); }
  .details__address { margin-bottom: 10px; }
  .contact { list-style: none; font-size: 20px; line-height: 28px; }
  .contact li { display: flex; align-items: center; gap: 10px; }
  .contact svg { width: 18px; height: 18px; flex: none; fill: none; stroke: var(--brand-blue); stroke-width: 1.8; }
  .contact svg .solid { fill: var(--brand-blue); stroke: none; }
</style>
</head>
<body>
<main class="sheet">
  <section class="card card--back" aria-label="Card back">
    <div class="wordmark wordmark--back"><span class="wordmark__dot"></span>QUORENTA</div>
  </section>

  <section class="card card--front" aria-label="Card front">
    <div class="wordmark wordmark--front"><span class="wordmark__dot"></span>QUORENTA</div>
    <div class="divider"></div>
    <div class="details">
      <p class="details__name">Lotta Berglund</p>
      <p class="details__role">Chief Financial Officer (CFO)</p>
      <p class="details__company">Quorenta Sweden AB</p>
      <p class="details__address">Rönnvägen 14<br>SE-175 43 JÄRFÄLLA, Sweden</p>
      <ul class="contact">
        <li><svg viewBox="0 0 18 18"><rect x="5" y="1.5" width="8" height="15" rx="1.5"/><line x1="8" y1="14" x2="10" y2="14"/></svg>+46701 23 45 67</li>
        <li><svg viewBox="0 0 18 18"><path class="solid" d="M4 1.5l3 3-1.6 2a9 9 0 0 0 6.1 6.1l2-1.6 3 3-2 2.5C8 16 2 10 1.5 3.5z"/></svg>+46 8 52 61 74</li>
        <li><svg viewBox="0 0 18 18"><rect x="1.5" y="4" width="15" height="10"/><polyline points="1.5,4 9,10 16.5,4"/></svg>lotta@quorenta-example.com</li>
        <li><svg viewBox="0 0 18 18"><circle cx="9" cy="9" r="7.5"/><ellipse cx="9" cy="9" rx="3.2" ry="7.5"/><line x1="1.5" y1="9" x2="16.5" y2="9"/></svg>www.quorenta-example.com</li>
      </ul>
    </div>
  </section>
</main>
</body>
</html>
```